Blue Heron Courier & Delivery Services needs a flyer

We need an introductory flyer for a new company based in Yellowknife, Northwest Territories,Canada. Our company name is Blue Heron Courier & Delivery Services. We will be handling envelopes and small packages up to 20 pounds. We expect 20 percent of our business to come from residential customers and 80 percent from the business community including lawyers, doctors, engineers and government offices. The main message that we will try to convey in this flyer is that we are a new and exciting company that promises to make 100% customer satisfaction our number one goal. I would like the layout to be elegant and simple and certainly not cluttered. It will be a single sided flyer. Text should be easy to read and most likely at most two fonts. I would like one stunning image or photo relating to the courier business and message. There should be plenty of white space throughout the flyer and nice margins on all sides. I would like my flyer to be 8.5 inches by 11 inches and it should read from top to bottom. . I would like a nice big bold headline that in some way mentions " Special Offer- Up to 100% Off. You can change the wording if you have a better idea. Throughout the flyer you can highlight and italicize for emphasis. Please try to use bullet points for my five main reasons for hiring our company which are: you will be 100% satisfied with each delivery or you will be given a complete refund no questions asked, your envelope or package will be delivered on time every time, you will always be treated throughout the delivery process in a professional manner, you will be given the widest selection in Yellowknife of price points and delivery options , you can trust us with your most important and time sensitive deliveries. Try to incorporate something next to these five points to really draw attention like a check mark, star etc.... I would prefer if my company name and contact info is in the bottom third of the flyer. My email is blueheroncourieryk@mailbox-example.net. My phone number is 867-312-7794. It might be a good idea to have my phone number also at the top of the flyer someplace after the headline saying like Call Now!!! you can use boxes, borders and contrasting bold colors to bring flyer to life. I have a testimonial from a business owner that I dealt with when I ran another business which would be nice to have included . " While receiving daily deliveries for 18 years from Calvin Marsh I found him to be punctual , reliable and efficient " Glen Potter, owner of Potter and Lindqvist Trading LTD, Yellowknife,NWT. I thought perhaps at the top of flyer after the headline perhaps in some way you could say Yellowknife's newest and best courier and delivery service is pleased to offer the following stunning discounts: then you could list the three special offers: 1) First 5 businesses to book regular scheduled deliveries will get 100% off their first delivery. 2) First 5 businesses to book a single delivery will get 50% off that delivery. 3) First 5 residential customers to book a delivery will receive 25% off that delivery. I thought you could mention my name somewhere. Calvin Marsh. Owner has lived in Yellowknife for 42 years and has 20 years experience doing performing important and time sensitive deliveries. Perhaps you could mention somewhere that we will have a couple of ongoing discounts also which will be 1) seniors discounts. 2) regular scheduled deliveries discounts. I have suggested colors but if you have other ideas I would certainly look at them. Our business tag line is. On Time Every Time
Target Market(s)
Business owners typically males 30-50 years old
Industry/Entity Type
Delivery Service
Requirements
Must have
- Done in CMYK mode sufficient bleed size for printing
Nice to have
- Nothing set in stone. I recently had my logo design uploaded to this brief. It is up to you if you feel it should be included in the flyer.
Should not have
- I am willing to look at any design

```html
<!DOCTYPE html>
<html lang="en">
<head>
<meta charset="utf-8">
<title>Blue Heron Courier &amp; Delivery Services – Flyer</title>
<link rel="stylesheet" href="https://fonts.googleapis.com/css2?family=Oswald:wght@300;400&family=Noto+Sans:wght@400&display=swap">
<style>
  :root {
    --orange: #f37a2e;
    --orange-text: #f07b2c;
    --brown: #a8420f;
    --red-deep: #8c0e0e;
    --red: #c8201c;
    --green: #4a6b12;
    --green-dark: #3d5a0c;
    --sage: #dde3cf;
    --ink: #3a3a22;
    --white: #ffffff;
    --backdrop: #eceae6;
  }
  * { box-sizing: border-box; margin: 0; padding: 0; }
  html, body { width: 1200px; height: 1000px; overflow: hidden; background: var(--backdrop); }
  .flyer {
    position: absolute; left: 248px; top: 31px;
    width: 640px; height: 852px;
    transform: scale(1.1); transform-origin: 0 0;
    background: var(--white);
    box-shadow: 0 4px 14px rgba(0,0,0,.18);
    font-family: "Noto Sans", Verdana, sans-serif;
    overflow: hidden;
  }
  .abs { position: absolute; }
  .header { left: 0; top: 0; width: 640px; height: 152px; background: var(--orange); }
  .title {
    left: 0; width: 470px; text-align: center;
    font-family: "Oswald", "Arial Narrow", sans-serif; font-weight: 300;
    color: var(--white); font-size: 46px; line-height: 1; letter-spacing: .5px;
  }
  .title-rule { left: 28px; width: 420px; height: 1px; background: rgba(255,255,255,.7); }
  .badge { left: 470px; top: -20px; width: 170px; height: 170px; }
  .badge-text {
    left: 470px; top: 8px; width: 170px; text-align: center;
    color: var(--white); font-size: 24px; line-height: 32px;
  }
  .hero {
    left: 0; top: 152px; width: 460px; height: 173px;
    background: linear-gradient(180deg, #ffffff 0%, #f2f2f2 55%, #d9d9d9 100%);
  }
  .satisfaction {
    left: 5px; top: 160px; width: 245px; height: 98px;
    background: var(--green-dark); border: 2px solid #c9d1b4;
    color: var(--white); font-size: 18px; line-height: 38px; text-align: center;
    padding-top: 10px;
  }
  .phone-icon { left: 508px; top: 192px; width: 32px; height: 24px; }
  .phone { left: 444px; top: 222px; color: var(--orange-text); font-size: 25px; }
  .address { left: 466px; top: 252px; color: var(--ink); font-size: 14.5px; line-height: 25px; }
  .offers-title { left: 0; top: 334px; width: 626px; text-align: center; color: var(--brown); font-size: 23px; }
  .offers { left: 22px; top: 364px; width: 600px; list-style: none; color: var(--brown); font-size: 17.5px; line-height: 26px; }
  .offers li { position: relative; padding-left: 23px; }
  .offers li svg { position: absolute; left: 0; top: 1px; }
  .tag { height: 31px; color: var(--white); font-size: 18px; line-height: 31px; }
  .tag-shape { left: 0; top: 0; }
  .tag-label { position: absolute; top: 0; }
  .promises-tag { left: 450px; top: 489px; width: 190px; }
  .panel { background: var(--sage); }
  .promises { left: 7px; top: 522px; width: 628px; height: 180px; }
  .promise-list { left: 13px; top: 528px; width: 620px; list-style: none; color: var(--ink); font-size: 14.5px; line-height: 25.3px; }
  .promise-list li { position: relative; padding-left: 27px; }
  .promise-list li.arrow svg { position: absolute; left: 0; top: 6px; }
  .discounts-tag { left: 5px; top: 704px; width: 190px; }
  .discounts-intro { left: 25px; top: 735px; color: var(--ink); font-size: 19px; }
  .discount-panel { left: 7px; top: 762px; width: 628px; height: 60px; }
  .discount-list { left: 14px; top: 764px; list-style: none; color: var(--ink); font-size: 18.5px; line-height: 26px; }
  .discount-list li { position: relative; padding-left: 26px; }
  .discount-list li svg { position: absolute; left: 0; top: 2px; }
  .email { right: 8px; top: 816px; color: var(--brown); font-size: 13.5px; }
  .footer-band { left: 0; top: 837px; width: 640px; height: 15px; background: var(--green); }
</style>
</head>
<body>
<main class="flyer">
  <div class="abs header"></div>
  <h1 class="abs title" style="top:24px">BLUE HERON COURIER</h1>
  <div class="abs title-rule" style="top:75px"></div>
  <p class="abs title" style="top:92px">&amp;&nbsp; DELIVERY&nbsp; SERVICES</p>
  <div class="abs title-rule" style="top:141px"></div>

  <svg class="abs badge" viewBox="0 0 170 170" aria-hidden="true">
    <defs>
      <radialGradient id="badgeFill" cx="50%" cy="40%" r="60%">
        <stop offset="0" stop-color="#e24a3c"/>
        <stop offset="1" stop-color="#8c0e0e"/>
      </radialGradient>
    </defs>
    <polygon fill="url(#badgeFill)" points="85,5 98,20 116,9 122,28 142,24 140,44 160,48 150,65 167,77 153,90 164,106 145,112 149,132 129,131 124,151 106,143 95,160 85,148 75,160 64,143 46,151 41,131 21,132 25,112 6,106 17,90 3,77 20,65 10,48 30,44 28,24 48,28 54,9 72,20"/>
  </svg>
  <p class="abs badge-text">Special<br>Offer<br>Up to 100%<br>off.</p>

  <div class="abs hero" role="img" aria-label="Photo of a white delivery truck beside a courier leaning on a hand truck stacked with parcels"></div>
  <div class="abs satisfaction">100% customer<br>satisfaction</div>

  <svg class="abs phone-icon" viewBox="0 0 32 24" aria-hidden="true">
    <path fill="#f37a2e" d="M2 7 Q16 -2 30 7 L28 11 L22 10 L21 6 Q16 4 11 6 L10 10 L4 11 Z"/>
    <path fill="#f37a2e" d="M8 12 L24 12 L27 23 L5 23 Z"/>
    <circle cx="16" cy="17" r="3" fill="#fff"/>
  </svg>
  <p class="abs phone">867-312-7794</p>
  <p class="abs address">Yellowknife,<br>Northwest Territories,<br>Canada.</p>

  <h2 class="abs offers-title" style="font-weight:400">THREE SPECIAL OFFERS</h2>
  <ul class="abs offers">
    <li><svg width="20" height="22" viewBox="0 0 20 22"><path fill="#f37a2e" d="M1 12 L5 10 L8 15 L17 1 L20 2 L9 21 Z"/></svg>First 5 businesses to book regular scheduled deliveries will get 100% off their first delivery.</li>
    <li><svg width="20" height="22" viewBox="0 0 20 22"><path fill="#f37a2e" d="M1 12 L5 10 L8 15 L17 1 L20 2 L9 21 Z"/></svg>First 5 businesses to book a single delivery will get 50% off that delivery.</li>
    <li><svg width="20" height="22" viewBox="0 0 20 22"><path fill="#f37a2e" d="M1 12 L5 10 L8 15 L17 1 L20 2 L9 21 Z"/></svg>First 5 residential customers to book a delivery will receive 25% off that delivery.</li>
  </ul>

  <div class="abs panel promises"></div>
  <div class="abs tag promises-tag">
    <svg class="abs tag-shape" width="190" height="31" viewBox="0 0 190 31" aria-hidden="true">
      <polygon fill="#4a6b12" points="14,0 155,0 155,31 14,31 0,15.5"/>
      <rect x="155" y="0" width="9" height="31" fill="#c8201c"/>
      <rect x="164" y="0" width="17" height="31" fill="#fff"/>
      <rect x="181" y="0" width="9" height="31" fill="#c8201c"/>
      <rect x="168" y="11" width="9" height="9" fill="#c8201c"/>
    </svg>
    <span class="tag-label" style="left:23px">5 PROMISES</span>
  </div>
  <ul class="abs promise-list">
    <li class="arrow"><svg width="18" height="12" viewBox="0 0 18 12"><path fill="#f37a2e" d="M0 0 L18 6 L0 12 L5 6 Z"/></svg>you will be 100% satisfied with each delivery or</li>
    <li>you will be given a complete refund no questions asked,</li>
    <li class="arrow"><svg width="18" height="12" viewBox="0 0 18 12"><path fill="#f37a2e" d="M0 0 L18 6 L0 12 L5 6 Z"/></svg>your envelope or package will be delivered on time every time,</li>
    <li class="arrow"><svg width="18" height="12" viewBox="0 0 18 12"><path fill="#f37a2e" d="M0 0 L18 6 L0 12 L5 6 Z"/></svg>you will be treated throughout the delivery process in a professional&nbsp; manner,</li>
    <li class="arrow"><svg width="18" height="12" viewBox="0 0 18 12"><path fill="#f37a2e" d="M0 0 L18 6 L0 12 L5 6 Z"/></svg>you will be given the widest selection in Yellowknife of price points and delivery</li>
    <li>options ,</li>
    <li class="arrow"><svg width="18" height="12" viewBox="0 0 18 12"><path fill="#f37a2e" d="M0 0 L18 6 L0 12 L5 6 Z"/></svg>you can trust us with your most important and time sensitive deliveries.</li>
  </ul>

  <div class="abs tag discounts-tag">
    <svg class="abs tag-shape" width="190" height="31" viewBox="0 0 190 31" aria-hidden="true">
      <rect x="0" y="0" width="9" height="31" fill="#c8201c"/>
      <rect x="9" y="0" width="17" height="31" fill="#fff"/>
      <rect x="26" y="0" width="9" height="31" fill="#c8201c"/>
      <rect x="13" y="11" width="9" height="9" fill="#c8201c"/>
      <polygon fill="#4a6b12" points="35,0 176,0 190,15.5 176,31 35,31"/>
    </svg>
    <span class="tag-label" style="left:44px">DISCOUNTS</span>
  </div>
  <p class="abs discounts-intro">we will have a couple of ongoing discounts also which will be</p>
  <div class="abs panel discount-panel"></div>
  <ul class="abs discount-list">
    <li><svg width="22" height="24" viewBox="0 0 20 22"><path fill="#3d5a0c" d="M1 12 L5 10 L8 15 L17 1 L20 2 L9 21 Z"/></svg>seniors discounts.</li>
    <li><svg width="22" height="24" viewBox="0 0 20 22"><path fill="#3d5a0c" d="M1 12 L5 10 L8 15 L17 1 L20 2 L9 21 Z"/></svg>Regular scheduled deliveries discounts.</li>
  </ul>

  <p class="abs email">blueheroncourieryk@mailbox-example.net</p>
  <div class="abs footer-band"></div>
</main>
</body>
</html>
```